Design homepage Ticketing for events

We need a single HTML + CSS homepage of ticketing selling event.
Just 1 page very simple but very strong impact

This is a page event where it's possible to buy a ticket ( [login to view URL] ) NOW WE NEED A HOMEPAGE WITH ALL EVENTS

The homepage have show the list of events that people can buy and the features of the ticketing system.

*** VERY IMPORTANT MOBILE VERSION****
IT WILL BE RESPONSIVE AND IOS STYLE WITH BORDER ROUNDED.

Ideal Color: RED ( #ff3d3e ) BLUE ( #2b3643 )

The page must contain:
1) Header with logo of company, search box for find event and static link page like About us, Contact, etc
2) Slider bar with events
3) Search bar find event or place like city or club ( with icon as you choose )
4) List events
5) List new events entry
6) Social icons
7) Banner
8) System features (PAPERLESS / PRIORITY PASS / NO SPAM / ASSISTENZA IMMEDIATA )
9) Are you an organizer (B2B) ? use PassoVela
10) PassoVela features for B2B ( Sell ticket / 1 minuti to ready and sell ticket / Checkin at the door / Analyze)
11) Footer with menu etc

Attach competitor design:
[login to view URL]
[login to view URL]
[login to view URL]
[login to view URL]
[login to view URL]
[login to view URL]
[login to view URL]
[login to view URL]
[login to view URL]

```html
<!DOCTYPE html>
<html lang="en">
<head>
<meta charset="utf-8">
<title>PassoVela – Event Tickets</title>
<link href="https://fonts.googleapis.com/css2?family=Roboto:ital,wght@0,300;0,400;0,500;0,700;1,400;1,700&display=swap" rel="stylesheet">
<style>
:root{
  --red:#f2413d;
  --red-soft:#ff3d3e;
  --yellow:#f7b71d;
  --dark:#1d1d1d;
  --darker:#111;
  --ink:#222;
  --muted:#8a8a8a;
  --blush:#fbf5f5;
  --green:#2bb673;
  --blue:#1f7fd8;
  --orange:#f39a1c;
  --purple:#7b4fc9;
  --teal:#19b394;
}
*{box-sizing:border-box;margin:0;padding:0}
html,body{width:1200px;height:4072px;overflow:hidden}
body{font-family:"Roboto",sans-serif;color:var(--ink);background:#fff;position:relative}
.abs{position:absolute}
a{color:inherit;text-decoration:none}

/* hero */
.hero{position:absolute;left:0;top:0;width:1200px;height:492px;
  background:linear-gradient(180deg,#3c4a3e 0%,#4a4a36 35%,#3a3026 70%,#2a221c 100%)}
.hero-topbar{position:absolute;left:36px;top:12px;font-size:10px;color:#eee;display:flex;gap:18px}
.hero-topbar span::before{content:"";display:inline-block;width:6px;height:6px;border-radius:50%;background:var(--yellow);margin-right:6px}
.hero-social{position:absolute;left:896px;top:13px;display:flex;gap:22px}
.hero-social i{width:9px;height:9px;border-radius:50%;background:#eee;display:block}
.hero-search{position:absolute;left:992px;top:13px;font-size:10px;line-height:12px;color:var(--yellow);font-weight:500}
.hero-search-btn{position:absolute;left:1148px;top:10px;width:28px;height:28px;background:var(--red);display:flex;align-items:center;justify-content:center}
.navbar{position:absolute;left:36px;top:47px;width:1140px;height:51px;background:rgba(0,0,0,.35)}
.logo{position:absolute;left:8px;top:10px;font-size:26px;font-weight:700;color:#fff;letter-spacing:-.5px}
.nav{position:absolute;right:12px;top:19px;display:flex;gap:30px;font-size:9px;font-weight:700;color:#fff;letter-spacing:.6px}
.caption{position:absolute;left:0;width:1200px;top:244px;text-align:center;font-size:30px;font-weight:300;color:#fff}
.caption b{font-weight:300;background:var(--yellow);padding:0 8px}
.caption-meta{position:absolute;left:0;width:1200px;top:294px;text-align:center;font-size:11px;letter-spacing:4px;color:#eee}
.hero-btn{position:absolute;top:332px;height:29px;width:76px;background:#fff;border:2px solid #e27c7c;border-radius:3px;font-size:8px;font-weight:700;display:flex;align-items:center;justify-content:center;color:#333}
.hero-dots{position:absolute;left:1144px;top:230px;display:flex;flex-direction:column;gap:16px}
.hero-dots i{width:7px;height:7px;border-radius:50%;background:#fff;display:block}
.hero-dots i.on{background:var(--red)}

/* ongoing */
.h-red{color:var(--red);font-weight:700;font-size:29px;line-height:33px}
.ongoing-intro{position:absolute;left:490px;top:546px;width:380px;font-size:10px;line-height:19px;color:var(--muted);font-weight:300}
.ev-card{position:absolute;top:673px;width:158px;height:212px;background:#fff;box-shadow:0 0 3px rgba(0,0,0,.18)}
.ev-card .pic{position:absolute;left:0;top:0;width:158px;height:108px}
.ev-card h3{position:absolute;left:0;width:158px;text-align:center;top:114px;color:var(--red);font-size:14px;font-weight:500}
.ev-card p{position:absolute;left:8px;top:136px;font-size:10px;color:#333;font-weight:500;line-height:17px}
.ev-card p small{display:block;font-size:8px;font-weight:400}
.ev-card .btn{position:absolute;left:8px;top:175px;width:90px;height:26px;border:2px solid var(--yellow);border-radius:2px;font-size:8px;font-weight:700;display:flex;align-items:center;justify-content:center}
.arrow-c{position:absolute;top:740px;width:24px;height:24px;border:2px solid var(--red);border-radius:50%;display:flex;align-items:center;justify-content:center}

/* categories */
.sec-title{position:absolute;left:0;width:1200px;text-align:center;font-size:26px;font-weight:500;color:#222}
.sec-sub{position:absolute;left:0;width:1200px;text-align:center;font-size:10px;color:var(--muted)}
.cat{position:absolute;width:210px;text-align:center}
.cat svg{display:block;margin:0 auto}
.cat .name{font-size:11px;font-weight:500;margin-top:10px}
.cat .count{font-size:15px;margin-top:16px}
.cat .desc{font-size:9.5px;line-height:15px;color:#555;margin-top:12px}
.cat .btn{display:inline-block;margin-top:12px;background:var(--red);color:#fff;font-size:9px;font-weight:500;padding:7px 9px;border-radius:2px}

/* organizer */
.organizer{position:absolute;left:0;top:1543px;width:1200px;height:397px;background:var(--blush)}
.org-pic{position:absolute;left:250px;top:51px;width:319px;height:295px;border-radius:4px;box-shadow:0 6px 14px rgba(0,0,0,.3);
  background:linear-gradient(180deg,#1c2a4a 0%,#4a3a6a 45%,#c66b52 80%,#e8a05a 100%)}
.org-title{position:absolute;left:610px;top:63px;font-size:23px;color:#222}
.org-red{position:absolute;left:610px;top:99px;font-size:19px;font-weight:700;color:var(--red);line-height:22px}
.org-list{position:absolute;left:610px;top:152px;font-size:12px;font-style:italic;font-weight:700;list-style:none}
.org-list li{height:30px;color:var(--red);display:flex;align-items:flex-start;gap:6px}
.org-list li.lead{color:#222;height:31px}
.org-btn{position:absolute;left:857px;top:294px;width:92px;height:32px;background:var(--red);color:#fff;font-size:10px;display:flex;align-items:center;justify-content:center;border-radius:2px;box-shadow:0 3px 6px rgba(0,0,0,.2)}

/* new events */
.dark{position:absolute;left:0;top:1940px;width:1200px;height:650px;background:var(--dark)}
.dark-title{position:absolute;left:0;width:1200px;top:56px;text-align:center;color:#fff;font-size:29px;font-weight:500}
.tabs{position:absolute;left:240px;top:136px;width:718px;height:39px;display:flex}
.tabs div{flex:1;color:#fff;font-size:9px;font-weight:700;letter-spacing:1px;display:flex;align-items:center;justify-content:center}
.tabs .on{background:var(--red);position:relative}
.tabs .on::after{content:"";position:absolute;bottom:-6px;left:50%;margin-left:-6px;border:6px solid transparent;border-bottom:0;border-top-color:var(--red)}
.panel{position:absolute;left:240px;top:175px;width:718px;height:424px;border:1px solid #333}
.ne{position:absolute;width:300px;height:110px}
.ne .thumb{position:absolute;left:0;top:0;width:62px;height:46px;border:2px solid #fff}
.ne .title{position:absolute;left:70px;top:8px;font-size:10px;color:#fff}
.ne .sub{position:absolute;left:70px;top:22px;font-size:7.5px;color:#666}
.ne .left{position:absolute;left:0;width:258px;text-align:right;top:40px;font-size:9.5px;font-weight:700;color:#fff}
.ne .btn{position:absolute;left:193px;top:64px;width:72px;height:25px;background:var(--yellow);color:#222;font-size:9px;font-weight:500;display:flex;align-items:center;justify-content:center;border-radius:2px}

/* features */
.feat{position:absolute;width:175px}
.feat h4{font-size:19px;font-weight:700;display:flex;align-items:center;gap:5px;line-height:21px}
.feat p{font-size:9.5px;line-height:16px;color:#999;margin-top:6px;font-weight:300}

/* special */
.collage{position:absolute;left:240px;top:2967px;width:718px;height:252px}
.cell{position:absolute;width:180px;height:126px}
.special-text{position:absolute;left:631px;top:3165px}
.special-p{position:absolute;left:240px;top:3256px;width:718px;font-size:10px;line-height:19px;color:var(--muted);font-weight:300}

/* contact */
.contact{position:absolute;left:0;top:3360px;width:1200px;height:668px;background:var(--darker)}
.contact-title{position:absolute;left:0;width:1200px;top:62px;text-align:center;color:#fff;font-size:29px;font-weight:500}
.c-label{position:absolute;font-size:11px;color:var(--red)}
.field{position:absolute;background:#fff;font-size:8px;color:#999;padding:8px 8px}
.c-btn{position:absolute;top:363px;width:187px;height:30px;border:1px solid #bbb;color:#fff;font-size:8px;font-weight:700;letter-spacing:1px;display:flex;align-items:center;justify-content:center}
.info{position:absolute;left:678px;color:#fff}
.info b{position:absolute;left:47px;top:0;font-size:10px;font-weight:500}
.info span{position:absolute;left:47px;top:15px;font-size:8.5px;color:#999;white-space:nowrap}
.map{position:absolute;left:240px;top:434px;width:718px;height:187px;
  background:linear-gradient(160deg,#e6e2d6 0%,#d6dcc4 35%,#a9cbe6 55%,#9fc4e4 75%,#e3ddcc 100%)}
.footer{position:absolute;left:0;top:4028px;width:1200px;height:44px;background:#000;color:#fff;font-size:8px;font-weight:500;letter-spacing:.6px;display:flex;align-items:center;justify-content:center}
</style>
</head>
<body>

<!-- HERO -->
<section class="hero" role="img" aria-label="Visitors walking through a classical art gallery hall with framed paintings">
  <div class="hero-topbar"><span>Via Ardesia, 22, Italy</span><span>hello@passovela.example</span></div>
  <div class="hero-social"><i></i><i></i><i></i></div>
  <div class="hero-search">Search for<br>EVENT / ARTIST / LOCATION</div>
  <div class="hero-search-btn"><svg width="13" height="13" viewBox="0 0 14 14"><circle cx="6" cy="6" r="4.2" fill="none" stroke="#fff" stroke-width="2"/><path d="M9 9l4 4" stroke="#fff" stroke-width="2"/></svg></div>
  <div class="navbar">
    <div class="logo">PassoVela</div>
    <nav class="nav"><a>HOME</a><a>ABOUT</a><a>SPECIAL EVENTS</a><a>CONTACT</a></nav>
  </div>
  <div class="caption">Caption for <b>Art Gallery</b> Event Here.</div>
  <div class="caption-meta">City Name - 19/01/2019</div>
  <a class="hero-btn" style="left:492px">Know More ›</a>
  <a class="hero-btn" style="left:594px">Book Tickets ›</a>
  <div class="hero-dots"><i></i><i></i><i class="on"></i><i></i></div>
</section>

<!-- ONGOING EVENTS -->
<h2 class="abs h-red" style="left:278px;top:586px">ON GOING<br>EVENTS</h2>
<p class="ongoing-intro">We Find all the Awsome Events , in Your locality. faucibus viverra libero vel efficitur. Ut semper nisl ut laoreet ultrices. Maecenas dictum arcu purus, sit amet volutpat purus viverra sit amet. Quisque lacinia quam sed tortor interdum, malesuada congue nunc ornare. Cum sociis natoque penatibus et magnis dis parturient montes, nascetur ridiculus mus. In semper lorem eget tortor pulvinar ultrices.</p>
<div class="abs" style="left:240px;top:673px;width:3px;height:212px;background:#222"></div>
<a class="arrow-c" style="left:198px"><svg width="8" height="10" viewBox="0 0 8 10"><path d="M6 1L2 5l4 4" fill="none" stroke="#f2413d" stroke-width="2"/></svg></a>
<a class="arrow-c" style="left:976px"><svg width="8" height="10" viewBox="0 0 8 10"><path d="M2 1l4 4-4 4" fill="none" stroke="#f2413d" stroke-width="2"/></svg></a>

<article class="ev-card" style="left:258px">
  <div class="pic" role="img" aria-label="Event poster in pink and green" style="background:linear-gradient(120deg,#e8408a,#3aa86c)"></div>
  <h3>Event Name</h3><p>Place of Event<small>21/01/2019</small></p><a class="btn">Book Tickets ›</a>
</article>
<article class="ev-card" style="left:438px">
  <div class="pic" role="img" aria-label="Bold black and white indie event poster" style="background:linear-gradient(180deg,#f2f2f2,#cfcfcf)"></div>
  <h3>Event Name</h3><p>Place of Event<small>21/01/2019</small></p><a class="btn">Book Tickets ›</a>
</article>
<article class="ev-card" style="left:618px">
  <div class="pic" role="img" aria-label="Dark DJ night event poster" style="background:linear-gradient(180deg,#2b2b2b,#5a5a5a)"></div>
  <h3>Event Name</h3><p>Place of Event<small>21/01/2019</small></p><a class="btn">Book Tickets ›</a>
</article>
<article class="ev-card" style="left:798px">
  <div class="pic" role="img" aria-label="Black and white performer portrait poster" style="background:linear-gradient(180deg,#3a3a3a,#8a8a8a)"></div>
  <h3>Event Name</h3><p>Place of Event<small>21/01/2019</small></p><a class="btn">Book Tickets ›</a>
</article>

<!-- CATEGORIES -->
<h2 class="sec-title" style="top:1005px">EVENT BY CATEGORIES</h2>
<p class="sec-sub" style="top:1045px">Lorem ipsum dolor sit amet,vehicula vel sapien et</p>

<div class="cat" style="left:255px;top:1100px">
  <svg width="22" height="28" viewBox="0 0 22 28"><circle cx="11" cy="4" r="3.5" fill="var(--green)"/><path d="M2 7l6 5v15h6V12l6-5-2-2-6 4h-2L4 5z" fill="var(--green)"/></svg>
  <div class="name">Party</div><div class="count">52 Events</div>
  <div class="desc">Duis sit amet posuere justo, sit amet finibus urna. Aenean elementum diam nec laoreet sodales.</div><a class="btn">Explore Events</a>
</div>
<div class="cat" style="left:494px;top:1100px">
  <svg width="26" height="28" viewBox="0 0 26 28"><path d="M8 5l16-4v18" fill="none" stroke="var(--blue)" stroke-width="3"/><path d="M8 5v17" stroke="var(--blue)" stroke-width="3"/><circle cx="5" cy="22" r="4" fill="var(--blue)"/><circle cx="21" cy="19" r="4" fill="var(--blue)"/></svg>
  <div class="name">Music</div><div class="count">34 Events</div>
  <div class="desc">Duis sit amet posuere justo, sit amet finibus urna. Aenean elementum diam nec laoreet sodales.</div><a class="btn">Explore Events</a>
</div>
<div class="cat" style="left:734px;top:1100px">
  <svg width="28" height="28" viewBox="0 0 28 28"><path d="M26 2c-4 2-11 9-14 13l3 3c4-3 11-10 13-14z" fill="var(--red)"/><path d="M10 17c-4 0-6 3-6 6 0 2-2 3-3 3 5 1 12 0 12-6z" fill="var(--red)"/></svg>
  <div class="name">Art</div><div class="count">13 Events</div>
  <div class="desc">Duis sit amet posuere justo, sit amet finibus urna. Aenean elementum diam nec laoreet sodales.</div><a class="btn">Explore Events</a>
</div>
<div class="cat" style="left:255px;top:1317px">
  <svg width="40" height="28" viewBox="0 0 40 28"><circle cx="9" cy="18" r="7" fill="none" stroke="var(--orange)" stroke-width="3"/><circle cx="31" cy="18" r="7" fill="none" stroke="var(--orange)" stroke-width="3"/><path d="M9 18l7-10h11l4 10M16 8l4 10h-11M14 5h5" fill="none" stroke="var(--orange)" stroke-width="3"/></svg>
  <div class="name">Sports</div><div class="count">22 Events</div>
  <div class="desc">Duis sit amet posuere justo, sit amet finibus urna. Aenean elementum diam nec laoreet sodales.</div><a class="btn">Explore Events</a>
</div>
<div class="cat" style="left:494px;top:1317px">
  <svg width="26" height="28" viewBox="0 0 26 28"><path d="M6 1h19l-4 26H2z" fill="var(--purple)"/><path d="M9 8h11M8 13h11" stroke="#fff" stroke-width="2"/></svg>
  <div class="name">knowledge</div><div class="count">12 Events</div>
  <div class="desc">Duis sit amet posuere justo, sit amet finibus urna. Aenean elementum diam nec laoreet sodales.</div><a class="btn">Explore Events</a>
</div>
<div class="cat" style="left:734px;top:1317px">
  <svg width="26" height="28" viewBox="0 0 26 28"><path d="M10 2h6v9h9v6h-9v9h-6v-9H1v-6h9z" fill="var(--teal)"/></svg>
  <div class="name">Others</div><div class="count">56 Events</div>
  <div class="desc">Duis sit amet posuere justo, sit amet finibus urna. Aenean elementum diam nec laoreet sodales.</div><a class="btn">Explore Events</a>
</div>

<!-- ORGANIZER -->
<section class="organizer">
  <div class="org-pic" role="img" aria-label="Fireworks over a silhouetted figure at dusk"></div>
  <h2 class="org-title">Do You Iniciate the Spark?</h2>
  <p class="org-red">Are you an organizer (B2B)? use<br>PassoVela</p>
  <ul class="org-list">
    <li class="lead">PassoVela features for B2B</li>
    <li><svg width="11" height="11" viewBox="0 0 12 12"><path d="M1 5l5-4 5 4-5 6z" fill="#222"/></svg>Sell ticket</li>
    <li><svg width="11" height="11" viewBox="0 0 12 12"><circle cx="6" cy="6" r="4.5" fill="none" stroke="#222" stroke-width="1.6"/><path d="M6 3v3h2" stroke="#222" stroke-width="1.4" fill="none"/></svg>1 minuti to ready and sell ticket</li>
    <li><svg width="9" height="12" viewBox="0 0 9 12"><path d="M4.5 0a4.5 4.5 0 0 1 4.5 4.5C9 8 4.5 12 4.5 12S0 8 0 4.5A4.5 4.5 0 0 1 4.5 0z" fill="#222"/><circle cx="4.5" cy="4.5" r="1.6" fill="#fff"/></svg>Checkin at the door</li>
    <li><svg width="11" height="11" viewBox="0 0 12 12"><circle cx="5" cy="5" r="3.6" fill="none" stroke="#222" stroke-width="1.8"/><path d="M7.5 7.5l3.5 3.5" stroke="#222" stroke-width="2"/></svg>Analyze</li>
  </ul>
  <a class="org-btn">Learn more</a>
</section>

<!-- NEW EVENTS -->
<section class="dark">
  <h2 class="dark-title">NEW EVENTS <i>(SPECIAL TICKETS)</i></h2>
  <div class="tabs"><div class="on">MUSIC</div><div>ART</div><div>PARTY</div><div>OTHERS</div></div>
  <div class="panel">
    <div class="ne" style="left:30px;top:20px"><div class="thumb" role="img" aria-label="Colourful party poster" style="background:linear-gradient(120deg,#3a8bd6,#f0c24a)"></div><div class="title">LOREM IPSUM DOLOR............</div><div class="sub">With Wild Mushrooms And Asparagus</div><div class="left">Tickets Left-525/1000</div><a class="btn">Book Tickets</a></div>
    <div class="ne" style="left:370px;top:20px"><div class="thumb" role="img" aria-label="Black and white portrait poster" style="background:linear-gradient(180deg,#333,#888)"></div><div class="title">LOREM IPSUM DOLOR............</div><div class="sub">With Wild Mushrooms And Asparagus</div><div class="left">Tickets Left-101/1000</div><a class="btn">Book Tickets</a></div>
    <div class="ne" style="left:30px;top:148px"><div class="thumb" role="img" aria-label="Black and red rock poster" style="background:linear-gradient(180deg,#111,#b83232)"></div><div class="title">LOREM IPSUM DOLOR............</div><div class="sub">With Wild Mushrooms And Asparagus</div><div class="left">Tickets Sold</div><a class="btn">Call Enquiry</a></div>
    <div class="ne" style="left:370px;top:148px"><div class="thumb" role="img" aria-label="Black and white indie poster" style="background:linear-gradient(180deg,#eee,#bbb)"></div><div class="title">LOREM IPSUM DOLOR............</div><div class="sub">With Wild Mushrooms And Asparagus</div><div class="left">Tickets Left-503/1000</div><a class="btn">Book Tickets</a></div>
    <div class="ne" style="left:30px;top:276px"><div class="thumb" role="img" aria-label="Pink and green poster" style="background:linear-gradient(120deg,#e8408a,#3aa86c)"></div><div class="title">LOREM IPSUM DOLOR............</div><div class="sub">With Wild Mushrooms And Asparagus</div><div class="left">Tickets Left-222/1000</div><a class="btn">Book Tickets</a></div>
    <div class="ne" style="left:370px;top:276px"><div class="thumb" role="img" aria-label="Dark DJ night poster" style="background:linear-gradient(180deg,#222,#555)"></div><div class="title">LOREM IPSUM DOLOR............</div><div class="sub">With Wild Mushrooms And Asparagus</div><div class="left">Tickets Left-525/1000</div><a class="btn">Book Tickets</a></div>
  </div>
</section>

<!-- SYSTEM FEATURES -->
<h2 class="abs h-red" style="left:289px;top:2705px">SYSTEM<br>FEATURES</h2>
<div class="feat" style="left:549px;top:2655px"><h4 style="color:var(--green)"><svg width="9" height="15" viewBox="0 0 9 15"><rect x="1" y="1" width="7" height="13" rx="1.5" fill="none" stroke="var(--green)" stroke-width="1.8"/></svg>PAPERLESS</h4><p>Duis sit amet posuere justo, sit amet finibus urna. Aenean elementum diam nec laoreet sodales. Morbi vulputate tempor nisl nec tristique.</p></div>
<div class="feat" style="left:749px;top:2655px"><h4 style="color:var(--orange)"><svg width="17" height="16" viewBox="0 0 17 16"><path d="M8.5 0l2.6 5.3 5.9.8-4.3 4.1 1 5.8-5.2-2.8-5.2 2.8 1-5.8L0 6.1l5.9-.8z" fill="var(--orange)"/></svg>PRIORITY PASS</h4><p>Duis sit amet posuere justo, sit amet finibus urna. Aenean elementum diam nec laoreet sodales. Morbi vulputate tempor nisl nec tristique.</p></div>
<div class="feat" style="left:549px;top:2783px"><h4 style="color:var(--red)"><svg width="14" height="16" viewBox="0 0 14 16"><path d="M3 15V6M3 6V2.5a1.2 1.2 0 0 1 2.4 0V7M5.4 7V1.5a1.2 1.2 0 0 1 2.4 0V7M7.8 7V2.5a1.2 1.2 0 0 1 2.4 0V8M10.2 8V5a1.2 1.2 0 0 1 2.4 0v5c0 3-2 5-5 5H5" fill="none" stroke="var(--red)" stroke-width="1.5"/></svg>NO SPAM</h4><p>Duis sit amet posuere justo, sit amet finibus urna. Aenean elementum diam nec laoreet sodales. Morbi vulputate tempor nisl nec tristique.</p></div>
<div class="feat" style="left:749px;top:2783px"><h4 style="color:var(--blue)"><svg width="18" height="15" viewBox="0 0 18 15"><circle cx="5" cy="3.5" r="3" fill="var(--blue)"/><circle cx="13" cy="3.5" r="3" fill="var(--blue)"/><path d="M0 15c0-5 2-7 5-7s5 2 5 7zM8 15c0-5 2-7 5-7s5 2 5 7z" fill="var(--blue)"/></svg>ASSISTENZA<br>IMMEDIATA</h4><p>Duis sit amet posuere justo, sit amet finibus urna. Aenean elementum diam nec laoreet sodales. Morbi vulputate tempor nisl nec tristique.</p></div>

<!-- SPECIAL EVENTS -->
<div class="collage">
  <div class="cell" role="img" aria-label="Dark DJ night poster" style="left:0;top:0;background:linear-gradient(180deg,#2b2b2b,#6a6a6a)"></div>
  <div class="cell" role="img" aria-label="Bold indie event poster" style="left:180px;top:0;background:linear-gradient(180deg,#f4f4f4,#d0d0d0)"></div>
  <div class="cell" role="img" aria-label="Black and white performer portrait" style="left:359px;top:0;background:linear-gradient(90deg,#111,#777)"></div>
  <div class="cell" role="img" aria-label="Pink and green poster" style="left:538px;top:0;background:linear-gradient(120deg,#e8408a,#3aa86c)"></div>
  <div class="cell" role="img" aria-label="Pink and green poster" style="left:0;top:126px;background:linear-gradient(120deg,#e8408a,#3aa86c)"></div>
  <div class="cell" role="img" aria-label="Colourful party poster" style="left:180px;top:126px;background:linear-gradient(160deg,#3a8bd6,#f0c24a)"></div>
</div>
<h2 class="abs h-red" style="left:631px;top:3151px">SPECIAL<br>EVENTS</h2>
<p class="special-p">Etiam faucibus viverra libero vel efficitur. Ut semper nisl ut laoreet ultrices. Maecenas dictum arcu purus, sit amet volutpat purus viverra sit amet. Quisque lacinia quam sed tortor interdum, malesuada congue nunc ornare. Cum sociis natoque penatibus et magnis dis parturient montes, nascetur ridiculus mus. In semper lorem eget tortor pulvinar ultrices.</p>

<!-- CONTACT -->
<section class="contact">
  <h2 class="contact-title">CONTACT US</h2>
  <div class="c-label" style="left:257px;top:145px">Please fill this form to contact with us.</div>
  <div class="field" style="left:250px;top:177px;width:185px;height:31px">Name</div>
  <div class="field" style="left:455px;top:177px;width:185px;height:31px">Telephone</div>
  <div class="field" style="left:250px;top:219px;width:185px;height:30px">Email</div>
  <div class="field" style="left:455px;top:219px;width:185px;height:30px">Subject</div>
  <div class="field" style="left:250px;top:261px;width:390px;height:90px">Message...</div>
  <a class="c-btn" style="left:250px">SUBMIT</a>
  <a class="c-btn" style="left:453px">CLEAR</a>
  <div class="c-label" style="left:685px;top:145px">Contact Info</div>
  <div class="info" style="top:183px"><svg width="11" height="10" viewBox="0 0 11 10"><path d="M5.5 0L11 5H9.5v5h-3V7h-2v3h-3V5H0z" fill="#fff"/></svg><b>Visit us</b><span>Via Ardesia, 22, Italy</span></div>
  <div class="info" style="top:254px"><svg width="11" height="8" viewBox="0 0 11 8"><rect width="11" height="8" fill="#fff"/><path d="M0 0l5.5 4.5L11 0" fill="none" stroke="#111" stroke-width="1"/></svg><b>Mail us</b><span>hello@passovela.example</span></div>
  <div class="info" style="top:324px"><svg width="10" height="10" viewBox="0 0 10 10"><path d="M2 0l2 2.5-1.2 1.5c.6 1.4 1.8 2.6 3.2 3.2L7.5 6 10 8 8.5 10C4 9.5.5 6 0 1.5z" fill="#fff"/></svg><b>Call us</b><span>+000-555-0142</span></div>
  <div class="map" role="img" aria-label="Map of Europe centred on Italy"></div>
</section>

<footer class="footer">© 2019 PassoVela All rights reserved</footer>
</body>
</html>
```